Website Page Re-Design

I have 2 pages that need to be re-designed on my site. This is the site so you can take a look and get a feel for the layout etc, www.pvrathletics.com
I have included screen shots of the individual pages I want redone as well as some examples from other sites for ideas.

Homepage Story, would like the redo sunday file, to be made stunning, only the content, picture and share buttons need be altered the, would like and emphasis on intergrating the share buttons, the story page starts here http://www.pvrathletics.com/league/ball-hockey/mens/news-division/ so what is beingcreated is when the read more is clicked

Free Agent Forms:
Needs to be re-worked so that there isn't so much white space on the page.

Industry/Entity Type

News

Requirements
Must have
• share buttons to slick very well intergrated
Nice to have
• Share buttons to be top notch

```html
<!DOCTYPE html>
<html lang="en">
<head>
<meta charset="utf-8">
<title>PVR Athletics – Men's Ball Hockey Free Agent Registration</title>
<link href="https://fonts.googleapis.com/css2?family=Noto+Sans:ital,wght@0,400;0,700;1,400;1,700&display=swap" rel="stylesheet">
<style>
  :root{
    --page-green:#82b03e;
    --page-green-light:#a3cb64;
    --panel:#e4f1d6;
    --form-bg:#e5f2d6;
    --form-edge:#cbdcb8;
    --banner-top:#9cc75a;
    --banner-bottom:#5f8f22;
    --topnav:#fde57a;
    --ink:#333;
    --title:#555;
    --white:#fff;
    --black:#111;
    --check:#2d5a8a;
    --tick:#2a7a2a;
    --submit-top:#8dbb43;
    --submit-bottom:#5a8c1f;
    --reset-top:#666;
    --reset-bottom:#2e2e2e;
  }
  *{box-sizing:border-box;margin:0;padding:0}
  html,body{width:1200px;height:810px;overflow:hidden}
  body{
    position:relative;
    font-family:"Noto Sans",Verdana,sans-serif;
    color:var(--ink);
    background:radial-gradient(ellipse at 50% 15%,var(--page-green-light) 0%,var(--page-green) 65%);
  }
  .brand{position:absolute;left:131px;top:26px;display:flex;align-items:center;gap:10px;
    font-size:32px;font-weight:700;color:var(--white);letter-spacing:-.5px;line-height:40px}
  .brand-mark{width:22px;height:22px;background:var(--topnav);border-radius:3px}
  .top-nav{position:absolute;left:656px;top:0;width:413px;height:27px;background:var(--topnav);
    border-radius:0 0 8px 8px;display:flex;align-items:center;padding-left:10px;font-size:14px;color:var(--black)}
  .top-nav a{color:inherit;text-decoration:none;padding:0 15px;border-right:1px solid #555;line-height:20px}
  .top-nav a:last-child{border-right:0}
  .main-nav{position:absolute;left:511px;top:39px;width:558px;height:51px;background:var(--black);
    border-radius:8px 18px 6px 18px;display:flex;align-items:center;padding-left:24px;
    font-size:15px;font-style:italic;color:var(--white)}
  .main-nav a{color:inherit;text-decoration:underline;padding:0 11px;border-right:1px solid #777;line-height:18px}
  .main-nav a:last-child{border-right:0}
  .panel{position:absolute;left:131px;top:104px;width:938px;height:605px;background:var(--panel);
    border-radius:8px;box-shadow:0 2px 4px rgba(0,0,0,.25)}
  .banner{position:absolute;left:147px;top:116px;width:908px;height:108px;border-radius:5px;
    background:linear-gradient(var(--banner-top),var(--banner-bottom))}
  .banner-photo{position:absolute;left:17px;top:-12px;width:633px;height:120px;
    background:linear-gradient(90deg,#c9a98b,#b84a3c 40%,#d8c0a6 70%,#e6e0d6)}
  .social-btn{position:absolute;left:696px;top:23px;width:164px;height:63px;background:var(--black);
    border-radius:6px;display:flex;align-items:center;gap:13px;padding-left:16px;color:var(--white);
    font-size:16px;font-style:italic;line-height:17px;text-decoration:none}
  .social-btn .sq{width:33px;height:33px;background:#3d5fa0;border-radius:3px}
  .form-box{position:absolute;left:147px;top:234px;width:911px;height:462px;background:var(--form-bg);
    border:1px solid var(--form-edge);border-radius:6px}
  .form-title{position:absolute;left:22px;top:9px;font-size:17.5px;font-weight:700;font-style:italic;color:var(--title)}
  .label{position:absolute;font-size:12.5px;line-height:16px}
  .input{position:absolute;left:22px;width:321px;height:25px;border:1px solid #d6dccd;
    border-radius:3px;background:var(--white);box-shadow:inset 0 1px 2px rgba(0,0,0,.08)}
  .divider{position:absolute;left:391px;top:52px;height:311px;border-left:1px dotted #9aa88a}
  .box{position:absolute;left:478px;width:12px;height:12px;border:1px solid var(--check);background:var(--white)}
  .box svg{position:absolute;left:0;top:0}
  .actions{position:absolute;left:261px;top:399px;display:flex;gap:26px}
  .btn{width:120px;height:40px;border-radius:4px;color:var(--white);font-family:"Noto Sans",Verdana,sans-serif;font-size:20px;
    letter-spacing:.5px;display:flex;align-items:center;justify-content:center;border:1px solid rgba(0,0,0,.25)}
  .btn-submit{background:linear-gradient(var(--submit-top),var(--submit-bottom))}
  .btn-reset{background:linear-gradient(var(--reset-top),var(--reset-bottom))}
  .footer{position:absolute;left:131px;top:744px;font-size:10.5px;color:var(--white);letter-spacing:.5px}
</style>
</head>
<body>
  <div class="brand"><span class="brand-mark"></span>PVR Athletics</div>

  <nav class="top-nav">
    <a href="#">Home</a><a href="#">About Us</a><a href="#">FAQS</a><a href="#">Contact Us</a><a href="#">Jobs</a>
  </nav>

  <nav class="main-nav">
    <a href="#">Leagues</a><a href="#">Schedules &amp; More</a><a href="#">Register</a><a href="#">Pay</a><a href="#">Forum</a><a href="#">Sponsors</a>
  </nav>

  <div class="panel"></div>

  <div class="banner">
    <div class="banner-photo" role="img" aria-label="Row of league players in hockey jerseys and helmets"></div>
    <a class="social-btn" href="#"><span class="sq"></span><span>Find Us On<br>Huddle</span></a>
  </div>

  <form class="form-box">
    <h2 class="form-title">Men’s Ball Hockey Free Agent Registration</h2>

    <span class="label" style="left:22px;top:50px">Men’s Balll Hockey Free Agentt<br>First Name (* Required)</span>
    <input class="input" style="top:87px" type="text">
    <span class="label" style="left:23px;top:126px;font-style:italic">Last Name (* Required)</span>
    <input class="input" style="top:146px" type="text">
    <span class="label" style="left:23px;top:185px">Email Address (* Required)</span>
    <input class="input" style="top:205px" type="text">
    <span class="label" style="left:23px;top:244px">Cell Phone (*Required)</span>
    <input class="input" style="top:262px" type="text">
    <span class="label" style="left:22px;top:311px">Gender (*Required)</span>
    <input class="input" style="top:331px" type="text">

    <div class="divider"></div>

    <span class="label" style="left:473px;top:52px">Preferred Position (*Requireed)</span>
    <span class="box" style="top:81px"><svg width="10" height="10"><path d="M1.5 5l2.5 2.5 4.5-6" stroke="var(--tick)" stroke-width="1.8" fill="none"/></svg></span>
    <span class="label" style="left:499px;top:79px">Forward</span>
    <span class="box" style="top:103px"></span><span class="label" style="left:499px;top:101px">Defense</span>
    <span class="box" style="top:125px"></span><span class="label" style="left:499px;top:123px">Goalie</span>

    <span class="label" style="left:473px;top:164px">Skill Level (*Required)</span>
    <span class="box" style="top:189px"><svg width="10" height="10"><path d="M1.5 5l2.5 2.5 4.5-6" stroke="var(--tick)" stroke-width="1.8" fill="none"/></svg></span>
    <span class="label" style="left:500px;top:187px">Beginner</span>
    <span class="box" style="top:211px"></span><span class="label" style="left:500px;top:209px">Average</span>
    <span class="box" style="top:233px"></span><span class="label" style="left:500px;top:231px">All-Stars</span>

    <span class="label" style="left:473px;top:269px">How Should Teams Contact You (*Required)</span>
    <span class="box" style="top:295px"><svg width="10" height="10"><path d="M1.5 5l2.5 2.5 4.5-6" stroke="var(--tick)" stroke-width="1.8" fill="none"/></svg></span>
    <span class="label" style="left:500px;top:293px">Text Msg</span>
    <span class="box" style="top:317px"></span><span class="label" style="left:500px;top:315px">Call Me</span>
    <span class="box" style="top:339px"></span><span class="label" style="left:500px;top:337px">Email</span>

    <div class="actions">
      <button type="submit" class="btn btn-submit">Submit</button>
      <button type="reset" class="btn btn-reset">Reset</button>
    </div>
  </form>

  <footer class="footer">© 2011, PVR ATHLETICS. ALL RIGHTS RESERVED.</footer>
</body>
</html>
```